Range of 4 soft drink labels

The goal is to create a coherent sub-range, immediately identifiable as part of my beer universe, while assuming a lighter, more joyful and accessible personality.
common DNA of the 4 labels
Graphic style: modern, flat design enriched with light textures (grain, paper, micro-imperfections) to evoke the world of crafts.
Typography: a strong, legible, contemporary main typeface (sans-serif or grotesque), complemented by a more expressive or handwritten secondary typeface for the fun side.
Composition: clear structure, with a central axis or a block composition, similar to that of the beer range (same margins, same hierarchy logic).
Illustration: stylized, abstract or semi-figurative motifs (bubbles, plants, bursts, waves), avoiding realism to remain graphic and timeless.
Tone: joyful, refreshing, embracing pleasure without being childish.
Consistency: same label formats, same logic for name placement, same visual rhythm.
1. Cola – The iconic revisited
Color codes
Dominant deep red
Cream/ivory accents
Touches of black or dark brown for depth
Graphic intention
A cola that respects classic conventions but with a contemporary, artisanal touch. The red color is vibrant but slightly desaturated to avoid an industrial look.
Design
Textured red background, reminiscent of paper or ink.
Dynamic graphic patterns (curves, soft lightning bolts, stylized bubbles).
Robust, rounded typography with character.
A sensation of indulgence, roundness and energy.
Emotion
Confidence, pleasure, modernized nostalgia.
2. Tonic – Dry and elegant freshness
Color codes
Light blue, blue-grey or mineral blue
Off-white
Touches of silver or very light grey
Graphic intention
A clean, lively and elegant tonic, which evokes bitterness, freshness and finesse, without falling into cold luxury.
Design
A more airy composition than other soft drinks.
Patterns of fine bubbles, vertical lines or geometric shapes evoking tonicity.
Thinner or slightly condensed typography.
An immediate feeling of freshness.
Emotion
Freshness, precision, accessible sophistication.
3. Lemon-verbena lemonade – The refreshing botanical
Color codes
Pale yellow
Verbena green / sage green
Soft white
Graphic intention
Highlighting the natural and plant-based aspect, without falling into the organic cliché. A fresh, herbaceous, elegant drink.
Design
Stylized illustrations of verbena leaves and lemon peel.
Organic patterns, flowing lines.
Warm and contemporary typography.
A soft, luminous, slightly powdery palette.
Emotion
Nature, freshness, balance, craftsmanship.
4. Sparkling Lemonade – Sunshine and Energy
Color codes
Bright yellow dominant
Bright white
Touches of more acidic yellow or lime
Graphic intention
An ultra-fresh, cheerful and thirst-quenching lemonade that immediately catches the eye.
Design
Dynamic bubble patterns, bursts, circles.
A more rhythmic composition, almost in motion.
Expressive typography, slightly more playful.
Strong contrasts for an immediate visual impact.
Emotion
Sunshine, fun, a burst of freshness.
Consistency with the beer range (see www.kolvira.fr)
To ensure harmony with my existing range:
Same layout logic.
Same family of typefaces (dink / frail).
Same level of texture and detail.
Soft drinks appear as a lighter and more joyful version of the beer universe, not as a separate range.

```html
<!DOCTYPE html>
<html lang="en">
<head>
<meta charset="utf-8">
<title>Kolvira soft drink labels</title>
<link rel="stylesheet" href="https://fonts.googleapis.com/css2?family=Rubik+Dirt&family=Damion&display=swap">
<style>
  :root{
    --page:#ffffff;
    --ink-light:#f4f1ea;
    --cola-edge:#3e0404;
    --cola-mid:#7c0808;
    --cola-core:#b00f0f;
    --tonic-edge:#3b444a;
    --tonic-mid:#8d9196;
    --tonic-core:#c9cbce;
    --verbena-edge:#36473a;
    --verbena-mid:#5b7a4e;
    --verbena-core:#86a06a;
    --spark-edge:#5a9a0e;
    --spark-mid:#8cc31c;
    --spark-core:#c8de3a;
    --brand-dark:#39433c;
  }
  *{margin:0;padding:0;box-sizing:border-box}
  html,body{width:1200px;height:1200px;overflow:hidden;background:var(--page)}
  .sheet{position:relative;width:1200px;height:1200px}
  .label{
    position:absolute;width:372px;height:536px;
    border-radius:186px/200px;
    border:9px solid var(--edge);
    background:radial-gradient(ellipse at 50% 35%,var(--core) 0%,var(--mid) 55%,var(--mid) 80%,var(--edge) 130%);
    overflow:hidden;color:var(--ink-light);text-align:center;
  }
  .label::before,.label::after{
    content:"";position:absolute;border-radius:inherit;border:2px solid rgba(255,255,255,.18);
  }
  .label::before{inset:10px}
  .label::after{inset:22px;border-color:rgba(255,255,255,.12)}
  .label--cola{left:208px;top:50px;--edge:var(--cola-edge);--mid:var(--cola-mid);--core:var(--cola-core)}
  .label--tonic{left:624px;top:50px;--edge:var(--tonic-edge);--mid:var(--tonic-mid);--core:var(--tonic-core)}
  .label--verbena{left:208px;top:640px;--edge:var(--verbena-edge);--mid:var(--verbena-mid);--core:var(--verbena-core)}
  .label--sparkling{left:624px;top:640px;--edge:var(--spark-edge);--mid:var(--spark-mid);--core:var(--spark-core)}
  .brand{
    position:absolute;left:0;right:0;top:130px;
    display:flex;align-items:center;justify-content:center;gap:12px;
    font-family:"Rubik Dirt",sans-serif;font-size:58px;color:var(--brand-color,var(--brand-dark));
  }
  .brand__dot{width:22px;height:22px;border-radius:50%;background:var(--brand-color,var(--brand-dark))}
  .label--cola .brand{--brand-color:var(--ink-light)}
  .flavour{
    position:absolute;left:0;right:0;font-family:"Rubik Dirt",sans-serif;line-height:1;
    text-shadow:0 2px 3px rgba(0,0,0,.35);
  }
  .flavour--single{top:330px;font-size:84px}
  .flavour--double{top:300px;font-size:58px;line-height:1.08}
  .flavour--double.is-wide{font-size:46px;top:335px;line-height:1.12}
  .tagline{
    position:absolute;left:0;right:0;font-family:"Damion",cursive;font-size:42px;
  }
  .tagline--low{top:420px}
  .tagline--lower{top:440px}
  .bubbles{position:absolute;inset:0;pointer-events:none}
  .garnish{position:absolute;left:150px;top:455px;width:70px;height:40px;border-radius:50%;background:rgba(255,255,255,.12)}
</style>
</head>
<body>
<main class="sheet">

  <article class="label label--cola">
    <div class="brand"><span class="brand__dot"></span>KOLVIRA</div>
    <svg class="bubbles" viewBox="0 0 354 518" aria-hidden="true">
      <g fill="none" stroke="rgba(255,255,255,.35)" stroke-width="1.5">
        <circle cx="292" cy="294" r="28"/><circle cx="312" cy="334" r="12"/>
        <circle cx="316" cy="368" r="9"/><circle cx="94" cy="420" r="8"/><circle cx="72" cy="438" r="5"/>
      </g>
    </svg>
    <h2 class="flavour flavour--single">COLA</h2>
    <p class="tagline tagline--low">iconic</p>
  </article>

  <article class="label label--tonic">
    <div class="brand"><span class="brand__dot"></span>KOLVIRA</div>
    <svg class="bubbles" viewBox="0 0 354 518" aria-hidden="true">
      <g fill="none" stroke="rgba(255,255,255,.45)" stroke-width="1.5">
        <circle cx="304" cy="290" r="26"/><circle cx="316" cy="322" r="10"/><circle cx="194" cy="486" r="10"/>
      </g>
    </svg>
    <h2 class="flavour flavour--single">TONIC</h2>
    <p class="tagline tagline--low">soft drink</p>
  </article>

  <article class="label label--verbena">
    <div class="brand"><span class="brand__dot"></span>KOLVIRA</div>
    <svg class="bubbles" viewBox="0 0 354 518" aria-hidden="true">
      <g fill="none" stroke="rgba(255,255,255,.35)" stroke-width="1.5">
        <circle cx="46" cy="268" r="26"/><circle cx="68" cy="286" r="10"/><circle cx="78" cy="424" r="12"/>
      </g>
    </svg>
    <h2 class="flavour flavour--double">LEMON<br>VERBENA</h2>
    <p class="tagline tagline--lower">lemonade</p>
    <div class="garnish" role="img" aria-label="Faint verbena leaf motif"></div>
  </article>

  <article class="label label--sparkling">
    <div class="brand"><span class="brand__dot"></span>KOLVIRA</div>
    <svg class="bubbles" viewBox="0 0 354 518" aria-hidden="true">
      <g fill="none" stroke="rgba(255,255,255,.45)" stroke-width="1.5">
        <circle cx="296" cy="270" r="26"/><circle cx="272" cy="308" r="10"/>
      </g>
    </svg>
    <h2 class="flavour flavour--double is-wide">SPARKLING<br>LEMONADE</h2>
    <p class="tagline tagline--lower">ultra-fresh</p>
    <div class="garnish" role="img" aria-label="Faint lemon slice motif"></div>
  </article>

</main>
</body>
</html>
```